QDV Construction and Remodeling

Prefer a matte black card with some colors that pop, but subtle. Contact info. Show General Contractor professional way. Can you please remove renovations repairs maintenance off of my logo.

Target Market(s)

Property and business investors. Homeowners

Industry/Entity Type

Construction

Contact Information for Business Card

Name: Dorian Falkner, Title: CEO, Phone: 555-216-0394, Email: Dorian@QDVbuildTrx.com, website: www QDVbuildTrx.com

Font styles to use
Other font styles liked:
• Designer choose

Colors

Designer to choose colors to be used in the design.

Requirements
Must have
• Uniqueness. Double sided since it wont let me choose that. Professional look, be eye catching and catchy. QR code to my website
Nice to have
• Matte black background, subtle bright colors that pop, but I am open to anything. I also like black and gold with some red. Possible Harborton Ironclad logo colored stars somewhere around the logo or on the back. Just to rep my city
Should not have
• pink. Something you would see somewhere else. gif pictures or generated pictures.

```html
<!DOCTYPE html>
<html lang="en">
<head>
<meta charset="UTF-8">
<title>QDV Construction and Remodeling — Business Card</title>
<link rel="stylesheet" href="https://fonts.googleapis.com/css2?family=Poppins:wght@400;500;700;800&display=swap">
<style>
  :root {
    --stage: #1b1b1e;
    --card: #262729;
    --card-edge: #2e2f32;
    --ink-white: #f4f4f4;
    --ink-soft: #d9d9d9;
    --accent-red: #e0242b;
    --emboss: #4a4c50;
  }
  * { box-sizing: border-box; margin: 0; padding: 0; }
  html, body {
    width: 1200px; height: 800px; overflow: hidden;
    background: var(--stage);
    font-family: "Poppins", sans-serif;
  }
  .stage {
    width: 1200px; height: 800px;
    display: flex; flex-direction: column;
    align-items: center; justify-content: center; gap: 40px;
  }
  .card {
    width: 600px; height: 343px;
    background: var(--card);
    border-radius: 22px;
    box-shadow: 0 18px 40px rgba(0,0,0,.55), inset 0 0 0 1px var(--card-edge);
    position: relative;
    display: flex; align-items: center;
  }
  .card--front { justify-content: center; }
  .card--back { justify-content: space-between; padding: 0 40px 0 44px; }

  .wordmark { display: flex; align-items: center; gap: 12px; }
  .wordmark__text {
    font-weight: 800; line-height: 1.05; text-transform: uppercase;
    white-space: nowrap;
  }
  .wordmark__name { font-size: 64px; letter-spacing: 1px; display: block; }
  .wordmark__tag { font-size: 15px; letter-spacing: 2px; display: block; }
  .wordmark--emboss .wordmark__text { color: var(--emboss); }
  .wordmark--light .wordmark__name { font-size: 56px; }
  .wordmark--light .wordmark__tag { font-size: 12px; letter-spacing: 1.4px; }
  .wordmark--light .wordmark__text { color: var(--ink-white); }
  .wordmark__square { width: 20px; height: 20px; background: var(--accent-red); flex: none; }

  .contact { display: flex; flex-direction: column; gap: 4px; color: var(--ink-soft); white-space: nowrap; }
  .contact__name { font-size: 24px; font-weight: 400; color: var(--ink-white); line-height: 1.1; }
  .contact__surname { color: var(--accent-red); font-weight: 700; }
  .contact__title { font-size: 14px; margin-bottom: 18px; }
  .contact__row { display: flex; align-items: center; gap: 10px; font-size: 13px; line-height: 1.6; }
  .contact__icon { width: 14px; height: 14px; flex: none; }
</style>
</head>
<body>
<main class="stage">
  <section class="card card--front" aria-label="Card front">
    <div class="wordmark wordmark--emboss">
      <div class="wordmark__text">
        <span class="wordmark__name">QDV</span>
        <span class="wordmark__tag">Construction &amp; Remodeling</span>
      </div>
    </div>
  </section>

  <section class="card card--back" aria-label="Card back">
    <div class="wordmark wordmark--light">
      <span class="wordmark__square"></span>
      <div class="wordmark__text">
        <span class="wordmark__name">QDV</span>
        <span class="wordmark__tag">Construction &amp; Remodeling</span>
      </div>
    </div>

    <div class="contact">
      <p class="contact__name">Dorian <span class="contact__surname">Falkner</span></p>
      <p class="contact__title">CEO</p>
      <p class="contact__row">
        <svg class="contact__icon" viewBox="0 0 24 24" aria-hidden="true"><path fill="#e0242b" d="M6.6 10.8a15 15 0 0 0 6.6 6.6l2.2-2.2c.3-.3.7-.4 1-.2 1.1.4 2.3.6 3.6.6.6 0 1 .4 1 1V20c0 .6-.4 1-1 1A17 17 0 0 1 3 4c0-.6.4-1 1-1h3.5c.6 0 1 .4 1 1 0 1.3.2 2.5.6 3.6.1.3 0 .7-.2 1z"/></svg>
        555-216-0394
      </p>
      <p class="contact__row">
        <svg class="contact__icon" viewBox="0 0 24 24" aria-hidden="true"><rect x="2" y="5" width="20" height="14" rx="1.5" fill="#e0242b"/><path d="M3 6l9 7 9-7" fill="none" stroke="#262729" stroke-width="1.8"/></svg>
        Dorian@QDVbuildTrx.com
      </p>
      <p class="contact__row">
        <svg class="contact__icon" viewBox="0 0 24 24" aria-hidden="true"><g fill="none" stroke="#e0242b" stroke-width="2"><circle cx="12" cy="12" r="9"/><ellipse cx="12" cy="12" rx="4" ry="9"/><path d="M3 12h18"/></g></svg>
        www.QDVbuildTrx.com
      </p>
    </div>
  </section>
</main>
</body>
</html>
```